Web Site - Holloway-Strength.com

Design a 3 page web site for Holloway Strength. See attached design brief.
Holloway Strength - Web Site
www.holloway-strength.com

Design a 3 page web site for Holloway Strength, a small local fitness center that provided cardio and weights only (machines and free weights). There are no classes or other services offered at this facility. Holloway Strength is an affordable alternative to the big box, expensive fitness centers. It is small, local, convenient and a community oriented place to work out.
web site can be clean, simple and communicate basic information about the company and membership offers. Although the branding is black, orange and gray, the web site colors should be soft, light and neutral colors that will appeal to both men and women.
Text: Input generic text during design for each text area that will be modified later during the coding phase. The selected designer is expected to code the site and deliver all compressive files (images, files and code) for an unrestricted hand off and full ownership of all content by the client for future modifications by others.

Images
Images used can be generic royalty free images of people working out, on cardio machines, lifting on universal equipment, stretching or lifting weights or images with out people i.e a yoga mat, free weights, a row of cardio machines etc. This is an adults only facility - images can be a mix of men and women and of diverse multi ethnic backgrounds. Image of the actual gym are included below but should NOT be used on the web site.

Branding - See attached for vertical and horizontal logos for Holloway Strength. These can be used in any way and should be incorporated into the web site
WEB SITE OUTLINE
THREE web pages - Pages can be individual pages clicked through to each page from a navigation area but ALSO pages can be “blend together” into one long scrolling “home” or primary landing page.
1) Home Page with basic information
2) Membership Page (to be later integrated with Quillmark member software to show changing membership specials). - see example below - all text will change later
3) contact page - address - telephone number - google map directions
www.holloway-strength.com
Address:
Located in Tannery Brook Commons
418 E. Walnut Lane, Suite 305, Alder Falls PA 19077
Tel: 484-555-0172

Target Market(s)

Men and Women - Adults over 18,

Industry/Entity Type

Fitness, Work Out, Gym

Coding

Coded - Design and coding required

Number of Pages Required

3 page

Requirements
Must have
• See Project Brief
Should not have
• Dark Colors that feel too masculine

```html
<!DOCTYPE html>
<html lang="en">
<head>
<meta charset="utf-8">
<title>Contact Us – Holloway Strength</title>
<link href="https://fonts.googleapis.com/css2?family=Lexend:wght@400;500;600&family=DM+Sans:wght@400;500;600&display=swap" rel="stylesheet">
<style>
:root{
  --orange:#ff6a00;
  --ink:#1b1b1b;
  --muted:#6b6b6b;
  --line:#e2e2e2;
  --soft:#f5f5f5;
  --white:#ffffff;
  --dark:#2a2a2a;
  --link:#1a66d6;
}
*{box-sizing:border-box;margin:0;padding:0}
html,body{width:1200px;height:2939px;overflow:hidden}
body{position:relative;font-family:"DM Sans",sans-serif;color:var(--ink);background:var(--white)}
.abs{position:absolute}
h1,h2,h3,.heading{font-family:"Lexend",sans-serif;font-weight:500}
svg{display:block}

/* top bar */
.topbar{left:0;top:0;width:1200px;height:36px;background:var(--orange);color:#fff;font-size:11px}
.topbar .item{position:absolute;top:11px;display:flex;gap:7px;align-items:center}
.topbar .links{position:absolute;right:67px;top:11px;display:flex;gap:12px}
.topbar .links span+span{border-left:1px solid rgba(255,255,255,.6);padding-left:12px}

/* hero */
.hero{left:0;top:36px;width:1200px;height:433px;background:linear-gradient(180deg,#3a2a22 0%,#4a3428 45%,#2b2320 100%)}
.hero-ghost{left:0;width:1200px;top:150px;text-align:center;font-family:"Lexend",sans-serif;font-size:92px;font-weight:600;color:transparent;-webkit-text-stroke:1px rgba(255,255,255,.18);letter-spacing:2px}
.hero-title{left:0;width:1200px;top:222px;text-align:center;color:#fff;font-size:50px;font-weight:600}
.crumb{left:0;width:1200px;top:294px;display:flex;justify-content:center;align-items:center;gap:10px;color:#fff;font-size:17px}

/* nav */
.nav{left:66px;top:36px;width:1067px;height:67px;background:#fff;display:flex;align-items:center}
.brand{display:flex;align-items:center;gap:8px;margin-left:27px;font-family:"Lexend",sans-serif;font-weight:600;font-size:15px;color:var(--ink)}
.brand .dot{width:14px;height:14px;border-radius:50%;background:var(--orange)}
.nav .sep{position:absolute;left:154px;top:12px;width:1px;height:42px;background:var(--line)}
.menu{position:absolute;left:327px;top:24px;display:flex;align-items:center;gap:15px;font-size:15px;font-weight:500}
.menu i{width:4px;height:4px;border-radius:50%;background:var(--orange);display:block}
.menu .active{color:var(--orange);position:relative}
.menu .active:after{content:"";position:absolute;left:20px;right:20px;top:43px;height:3px;background:var(--orange)}
.join{position:absolute;right:22px;top:11px;width:144px;height:44px;border-radius:22px;background:var(--dark);color:#fff;font-size:13px;font-weight:600;display:flex;align-items:center;justify-content:center;gap:10px}

/* section labels */
.label{display:flex;align-items:center;gap:8px;color:var(--orange);font-size:15px;font-weight:600}

/* intro */
.intro-label{left:66px;top:555px}
.intro-title{left:66px;top:585px;font-size:40px;line-height:47px;width:560px}
.intro-text{left:688px;top:592px;width:445px;font-size:14px;line-height:19.5px;color:var(--muted)}

/* form */
.form-photo{left:0;top:732px;width:599px;height:542px;background:linear-gradient(135deg,#c98a63 0%,#a9694a 50%,#3e3a40 100%)}
.form-panel{left:599px;top:732px;width:601px;height:542px;background:var(--soft)}
.form-title{left:668px;top:793px;font-size:33px}
.field{position:absolute;background:#fff;border:1px solid var(--line);border-radius:3px;display:flex;align-items:center;gap:8px;padding-left:14px;font-size:12px;color:#555}
.field.msg{align-items:flex-start;padding-top:13px}
.send{left:668px;top:1161px;width:185px;height:52px;border-radius:26px;background:var(--orange);color:#fff;font-size:13px;font-weight:600;display:flex;align-items:center;justify-content:center;gap:12px}

/* find us */
.find-label{left:0;width:1200px;top:1360px;justify-content:center}
.find-title{left:0;width:1200px;top:1390px;text-align:center;font-size:41px;font-weight:600}
.card{position:absolute;top:1484px;width:339px;height:407px;border:1px solid var(--line);border-radius:6px;overflow:hidden;background:var(--soft);text-align:center}
.card .photo{height:195px}
.card .badge{position:absolute;left:122px;top:146px;width:96px;height:96px;border-radius:50%;background:var(--orange);display:flex;align-items:center;justify-content:center}
.card h3{margin-top:66px;font-size:28px;font-weight:500}
.card p{margin-top:12px;font-size:16px;line-height:23.5px;color:var(--muted)}

/* map */
.map{left:0;top:1983px;width:1200px;height:457px;background:linear-gradient(135deg,#e3ece2 0%,#dfe8e6 55%,#cfdbe6 100%)}
.map-info{left:66px;top:2010px;width:206px;height:86px;background:#fff;border-radius:3px;box-shadow:0 1px 4px rgba(0,0,0,.2);padding:12px 0 0 19px;font-size:13px}
.map-info .place{font-weight:500;color:#222}
.map-info .sub{font-size:10px;color:#666;margin-top:4px}
.map-info .larger{font-size:11px;color:var(--link);margin-top:12px}
.map-info .dir{position:absolute;right:13px;top:14px;font-size:11px;color:var(--link);display:flex;flex-direction:column;align-items:center;gap:2px}
.map-thumb{left:66px;top:2300px;width:92px;height:90px;background:#fff;border-radius:3px;box-shadow:0 1px 4px rgba(0,0,0,.2);padding:5px}
.map-thumb div{width:100%;height:100%;background:linear-gradient(135deg,#5a5f63,#2c2f32)}
.map-pin{left:859px;top:2214px}
.map-ctrl{position:absolute;left:1096px;width:36px;background:#fff;border-radius:18px;box-shadow:0 1px 4px rgba(0,0,0,.25);display:flex;flex-direction:column;align-items:center;justify-content:center}

/* footer */
.footer{left:0;top:2440px;width:1200px;height:499px;background:linear-gradient(160deg,#2a2624 0%,#3a2d25 40%,#7a3d14 75%,#b3500f 100%);color:#fff}
.f-brand{position:absolute;left:66px;top:80px;display:flex;align-items:center;gap:10px;font-family:"Lexend",sans-serif;font-weight:600;font-size:24px}
.f-brand .dot{width:20px;height:20px;border-radius:50%;background:var(--orange)}
.f-about{position:absolute;left:66px;top:130px;width:300px;font-size:15px;line-height:22px}
.socials{position:absolute;left:66px;top:219px;display:flex;gap:8px}
.socials span{width:40px;height:40px;background:var(--orange);display:block}
.f-col{position:absolute;top:71px}
.f-col h4{font-family:"Lexend",sans-serif;font-weight:500;font-size:19px}
.f-col h4:after{content:"";display:block;width:38px;height:3px;background:var(--orange);margin-top:10px}
.f-col ul{list-style:none;margin-top:18px}
.f-col li{display:flex;align-items:center;gap:10px;font-size:15px;height:35px}
.f-contact{width:240px}
.f-contact li{font-size:17px;align-items:flex-start;height:auto;margin-bottom:14px;line-height:22px}
.f-contact svg{margin-top:4px;flex:none}
.f-rule{position:absolute;left:0;top:425px;width:1200px;height:1px;background:rgba(255,255,255,.15)}
.f-copy{position:absolute;left:438px;top:453px;font-size:13px}
.f-legal{position:absolute;right:67px;top:453px;font-size:13px;display:flex;gap:12px}
.f-legal span+span{border-left:1px solid rgba(255,255,255,.5);padding-left:12px}
</style>
</head>
<body>

<!-- top bar -->
<div class="abs topbar">
  <div class="item" style="left:67px">
    <svg width="13" height="13" viewBox="0 0 24 24" fill="none" stroke="#fff" stroke-width="2"><path d="M22 16.9v3a2 2 0 0 1-2.2 2 19.8 19.8 0 0 1-8.6-3.1 19.5 19.5 0 0 1-6-6A19.8 19.8 0 0 1 2.1 4.2 2 2 0 0 1 4.1 2h3a2 2 0 0 1 2 1.7c.1 1 .4 1.9.7 2.8a2 2 0 0 1-.5 2.1L8 9.9a16 16 0 0 0 6 6l1.3-1.3a2 2 0 0 1 2.1-.4c.9.3 1.8.6 2.8.7a2 2 0 0 1 1.7 2z"/></svg>
    484-555-0172
  </div>
  <div class="item" style="left:198px">
    <svg width="13" height="13" viewBox="0 0 24 24" fill="none" stroke="#fff" stroke-width="2"><rect x="3" y="5" width="18" height="14" rx="2"/><path d="m3 7 9 6 9-6"/></svg>
    hello@holloway-strength.com
  </div>
  <div class="links"><span>Get Help</span><span>FAQ</span><span>Terms</span></div>
</div>

<!-- hero -->
<div class="abs hero" role="img" aria-label="Gym floor with weight machines under a dark overlay"></div>
<div class="abs hero-ghost" aria-hidden="true">CONTACT US</div>
<h1 class="abs hero-title">Start Your Fitness Journey Today</h1>
<div class="abs crumb">
  <span style="font-weight:500">Home</span>
  <svg width="14" height="12" viewBox="0 0 14 12" fill="none" stroke="#ff6a00" stroke-width="1.8"><path d="M2 1l5 5-5 5M7 1l5 5-5 5"/></svg>
  <span>CONTACT US</span>
</div>

<!-- navigation -->
<nav class="abs nav">
  <div class="brand"><span class="dot"></span>Holloway Strength</div>
  <div class="sep"></div>
  <div class="menu">
    <span>Home</span><i></i><span>About</span><i></i><span>Membership</span><i></i><span>Blog</span><i></i><span class="active">Contact Us</span>
  </div>
  <div class="join">JOIN NOW
    <svg width="12" height="12" viewBox="0 0 12 12" fill="none" stroke="#fff" stroke-width="1.8"><path d="M2 10 10 2M4 2h6v6"/></svg>
  </div>
</nav>

<!-- intro -->
<div class="abs label intro-label">
  <svg width="22" height="14" viewBox="0 0 22 14" fill="none" stroke="#ff6a00" stroke-width="2"><rect x="2" y="3" width="3" height="8"/><rect x="17" y="3" width="3" height="8"/><path d="M5 7h12M1 5v4M21 5v4"/></svg>
  CONTACT US
</div>
<h2 class="abs intro-title">Let's Start A Conversation Together</h2>
<p class="abs intro-text">Have questions about memberships, classes, or training programs? We’d love to hear from you. Reach out to our friendly team and we’ll get back to you as quickly as possible to help you start your fitness journey with HollowayStrength.</p>

<!-- contact form -->
<div class="abs form-photo" role="img" aria-label="Two members training on elliptical machines in a warm-lit gym"></div>
<div class="abs form-panel"></div>
<h2 class="abs form-title">Bring Your Vision to Life</h2>
<div class="field" style="left:668px;top:865px;width:225px;height:52px">
  <svg width="12" height="12" viewBox="0 0 24 24" fill="none" stroke="#555" stroke-width="2"><circle cx="12" cy="8" r="4"/><path d="M4 21c0-4 4-6 8-6s8 2 8 6"/></svg>First Name</div>
<div class="field" style="left:908px;top:865px;width:225px;height:52px">
  <svg width="12" height="12" viewBox="0 0 24 24" fill="none" stroke="#555" stroke-width="2"><rect x="3" y="5" width="18" height="14" rx="2"/><path d="m3 7 9 6 9-6"/></svg>Email</div>
<div class="field" style="left:668px;top:938px;width:225px;height:53px">
  <svg width="12" height="12" viewBox="0 0 24 24" fill="none" stroke="#555" stroke-width="2"><path d="M22 16.9v3a2 2 0 0 1-2.2 2 19.8 19.8 0 0 1-8.6-3.1 19.5 19.5 0 0 1-6-6A19.8 19.8 0 0 1 2.1 4.2 2 2 0 0 1 4.1 2h3a2 2 0 0 1 2 1.7c.1 1 .4 1.9.7 2.8a2 2 0 0 1-.5 2.1L8 9.9a16 16 0 0 0 6 6l1.3-1.3a2 2 0 0 1 2.1-.4c.9.3 1.8.6 2.8.7a2 2 0 0 1 1.7 2z"/></svg>Phone Number</div>
<div class="field" style="left:908px;top:938px;width:225px;height:53px">
  <svg width="12" height="12" viewBox="0 0 24 24" fill="none" stroke="#555" stroke-width="2"><path d="m6 9 6 6 6-6"/></svg>Select Services</div>
<div class="field msg" style="left:668px;top:1013px;width:465px;height:119px">
  <svg width="12" height="12" viewBox="0 0 24 24" fill="none" stroke="#555" stroke-width="2"><path d="M3 4h18l-9 16z"/></svg>Message</div>
<div class="abs send">SEND MESSAGE
  <svg width="12" height="12" viewBox="0 0 12 12" fill="none" stroke="#fff" stroke-width="1.8"><path d="M2 10 10 2M4 2h6v6"/></svg>
</div>

<!-- find us -->
<div class="abs label find-label">
  <svg width="22" height="14" viewBox="0 0 22 14" fill="none" stroke="#ff6a00" stroke-width="2"><rect x="2" y="3" width="3" height="8"/><rect x="17" y="3" width="3" height="8"/><path d="M5 7h12M1 5v4M21 5v4"/></svg>
  FIND US NOW
</div>
<h2 class="abs find-title">READY FOR WORKOUT</h2>

<div class="card" style="left:66px">
  <div class="photo" role="img" aria-label="Members riding stationary bikes" style="background:linear-gradient(135deg,#6d7478,#3d4246)"></div>
  <div class="badge"><svg width="42" height="42" viewBox="0 0 24 24" fill="none" stroke="#fff" stroke-width="1.8"><path d="M12 22s7-6.5 7-12a7 7 0 0 0-14 0c0 5.5 7 12 7 12z"/><circle cx="12" cy="10" r="3"/></svg></div>
  <h3>Location</h3>
  <p>Located in Tannery Brook Commons<br>418 E. Walnut Lane, Suite 305,<br>Alder Falls PA 19077</p>
</div>
<div class="card" style="left:431px">
  <div class="photo" role="img" aria-label="Man training on a chest press machine" style="background:linear-gradient(135deg,#8a4a2a,#3a3532)"></div>
  <div class="badge"><svg width="42" height="42" viewBox="0 0 24 24" fill="none" stroke="#fff" stroke-width="1.8"><path d="M22 16.9v3a2 2 0 0 1-2.2 2 19.8 19.8 0 0 1-8.6-3.1 19.5 19.5 0 0 1-6-6A19.8 19.8 0 0 1 2.1 4.2 2 2 0 0 1 4.1 2h3a2 2 0 0 1 2 1.7c.1 1 .4 1.9.7 2.8a2 2 0 0 1-.5 2.1L8 9.9a16 16 0 0 0 6 6l1.3-1.3a2 2 0 0 1 2.1-.4c.9.3 1.8.6 2.8.7a2 2 0 0 1 1.7 2z"/><path d="M15 3v6h6M21 3l-6 6"/></svg></div>
  <h3>Phone</h3>
  <p>484-555-0172<br>(+800 555 0199)</p>
</div>
<div class="card" style="left:795px">
  <div class="photo" role="img" aria-label="Woman working out on cardio equipment" style="background:linear-gradient(135deg,#4d5a5e,#23282b)"></div>
  <div class="badge"><svg width="42" height="42" viewBox="0 0 24 24" fill="none" stroke="#fff" stroke-width="1.8"><path d="M20 12V6a2 2 0 0 0-2-2H4a2 2 0 0 0-2 2v11a2 2 0 0 0 2 2h9"/><path d="m2 6 9 6 9-6M16 19h6M19 16l3 3-3 3"/></svg></div>
  <h3>Email</h3>
  <p>info@holloway-strength.com<br>team@holloway-strength.com</p>
</div>

<!-- map -->
<div class="abs map" role="img" aria-label="Map showing directions to the gym in Alder Falls, PA"></div>
<div class="abs map-info">
  <div class="place">Alder Falls</div>
  <div class="sub">Alder Falls, PA</div>
  <div class="larger">View larger map</div>
  <div class="dir">
    <svg width="12" height="12" viewBox="0 0 24 24" fill="none" stroke="#1a66d6" stroke-width="2.5"><path d="M12 22V12l-6-6M12 12l6-6M3 6h6M21 6h-6"/></svg>
    Direction
  </div>
</div>
<div class="abs map-thumb"><div role="img" aria-label="Street view preview of the gym interior"></div></div>
<svg class="abs map-pin" width="30" height="40" viewBox="0 0 24 32"><path d="M12 31s10-11 10-19a10 10 0 0 0-20 0c0 8 10 19 10 19z" fill="#111"/><circle cx="12" cy="12" r="4" fill="#fff"/></svg>
<div class="map-ctrl" style="top:2284px;height:34px">
  <svg width="16" height="16" viewBox="0 0 24 24" fill="none" stroke="#333" stroke-width="2"><circle cx="12" cy="12" r="4" fill="#333"/><circle cx="12" cy="12" r="8"/></svg>
</div>
<div class="map-ctrl" style="top:2324px;height:62px;gap:14px">
  <svg width="14" height="14" viewBox="0 0 14 14" stroke="#222" stroke-width="2"><path d="M7 1v12M1 7h12"/></svg>
  <svg width="14" height="14" viewBox="0 0 14 14" stroke="#222" stroke-width="2"><path d="M1 7h12"/></svg>
</div>

<!-- footer -->
<footer class="abs footer">
  <div class="f-brand"><span class="dot"></span>Holloway Strength</div>
  <p class="f-about">Holloway Strength is your local, affordable gym focused on simple, effective workouts in a welcoming community environment.</p>
  <div class="socials" aria-label="Social links"><span></span><span></span><span></span><span></span></div>

  <div class="f-col" style="left:433px">
    <h4>Quick Links</h4>
    <ul>
      <li><svg width="12" height="10" viewBox="0 0 14 12" fill="none" stroke="#ff6a00" stroke-width="2"><path d="M2 1l5 5-5 5M7 1l5 5-5 5"/></svg>Home</li>
      <li><svg width="12" height="10" viewBox="0 0 14 12" fill="none" stroke="#ff6a00" stroke-width="2"><path d="M2 1l5 5-5 5M7 1l5 5-5 5"/></svg>About Us</li>
      <li><svg width="12" height="10" viewBox="0 0 14 12" fill="none" stroke="#ff6a00" stroke-width="2"><path d="M2 1l5 5-5 5M7 1l5 5-5 5"/></svg>Membership</li>
      <li><svg width="12" height="10" viewBox="0 0 14 12" fill="none" stroke="#ff6a00" stroke-width="2"><path d="M2 1l5 5-5 5M7 1l5 5-5 5"/></svg>Our Blog</li>
      <li><svg width="12" height="10" viewBox="0 0 14 12" fill="none" stroke="#ff6a00" stroke-width="2"><path d="M2 1l5 5-5 5M7 1l5 5-5 5"/></svg>Contact Us</li>
      <li><svg width="12" height="10" viewBox="0 0 14 12" fill="none" stroke="#ff6a00" stroke-width="2"><path d="M2 1l5 5-5 5M7 1l5 5-5 5"/></svg>FAQ</li>
      <li><svg width="12" height="10" viewBox="0 0 14 12" fill="none" stroke="#ff6a00" stroke-width="2"><path d="M2 1l5 5-5 5M7 1l5 5-5 5"/></svg>Testimonial</li>
    </ul>
  </div>
  <div class="f-col" style="left:651px">
    <h4>Support</h4>
    <ul>
      <li><svg width="12" height="10" viewBox="0 0 14 12" fill="none" stroke="#ff6a00" stroke-width="2"><path d="M2 1l5 5-5 5M7 1l5 5-5 5"/></svg>Courses Near You</li>
      <li><svg width="12" height="10" viewBox="0 0 14 12" fill="none" stroke="#ff6a00" stroke-width="2"><path d="M2 1l5 5-5 5M7 1l5 5-5 5"/></svg>Certificate</li>
      <li><svg width="12" height="10" viewBox="0 0 14 12" fill="none" stroke="#ff6a00" stroke-width="2"><path d="M2 1l5 5-5 5M7 1l5 5-5 5"/></svg>Help Center</li>
      <li><svg width="12" height="10" viewBox="0 0 14 12" fill="none" stroke="#ff6a00" stroke-width="2"><path d="M2 1l5 5-5 5M7 1l5 5-5 5"/></svg>Help Center</li>
      <li><svg width="12" height="10" viewBox="0 0 14 12" fill="none" stroke="#ff6a00" stroke-width="2"><path d="M2 1l5 5-5 5M7 1l5 5-5 5"/></svg>Careers</li>
      <li><svg width="12" height="10" viewBox="0 0 14 12" fill="none" stroke="#ff6a00" stroke-width="2"><path d="M2 1l5 5-5 5M7 1l5 5-5 5"/></svg>Get Started</li>
    </ul>
  </div>
  <div class="f-col f-contact" style="left:894px">
    <h4>Contact Us</h4>
    <ul>
      <li><svg width="16" height="16" viewBox="0 0 24 24" fill="none" stroke="#ff6a00" stroke-width="2"><path d="M22 16.9v3a2 2 0 0 1-2.2 2 19.8 19.8 0 0 1-8.6-3.1 19.5 19.5 0 0 1-6-6A19.8 19.8 0 0 1 2.1 4.2 2 2 0 0 1 4.1 2h3a2 2 0 0 1 2 1.7c.1 1 .4 1.9.7 2.8a2 2 0 0 1-.5 2.1L8 9.9a16 16 0 0 0 6 6l1.3-1.3a2 2 0 0 1 2.1-.4c.9.3 1.8.6 2.8.7a2 2 0 0 1 1.7 2z"/></svg>484-555-0172</li>
      <li><svg width="16" height="16" viewBox="0 0 24 24" fill="none" stroke="#ff6a00" stroke-width="2"><rect x="3" y="5" width="18" height="14" rx="2"/><path d="m3 7 9 6 9-6"/></svg>hello@holloway-strength.com</li>
      <li><svg width="16" height="16" viewBox="0 0 24 24" fill="none" stroke="#ff6a00" stroke-width="2"><path d="M12 22s7-6.5 7-12a7 7 0 0 0-14 0c0 5.5 7 12 7 12z"/><circle cx="12" cy="10" r="3"/></svg>Located in Tannery Brook Commons 418 E. Walnut Lane, Suite 305, Alder Falls PA 19077</li>
    </ul>
  </div>

  <div class="f-rule"></div>
  <div class="f-copy">Copyright © 2026 HollowayStrength . All Rights Reserved.</div>
  <div class="f-legal"><span>Privacy Policy</span><span>Terms &amp; Condition</span></div>
</footer>

</body>
</html>
```